Velvet Harbor (A luxury Travel Website)

website text attached in document below

images also attached

feel free to use other images if needed

Target Market(s)

Luxury Seekers and wealthy couples / families

Industry/Entity Type

Luxury Travel

Coding

Coded - Design and coding required

Number of Pages Required

1 page

Requirements
Must have
• A luxury design and easy use.
Nice to have
• Ease of use of page, incorporation of images into the flow of the site

```html
<!DOCTYPE html>
<html lang="en">
<head>
<meta charset="utf-8">
<title>Velvet Harbor — Luxury Travel</title>
<link rel="stylesheet" href="https://fonts.googleapis.com/css2?family=Questrial&family=Montserrat:wght@500;600;700&display=swap">
<style>
:root{
  --navy:#0f3e6b;
  --deep-blue:#1a5a92;
  --sky:#3aa8dc;
  --accent-text:#1c5e96;
  --ink:#1d1d1f;
  --muted:#8a8a8a;
  --line:#d8dde3;
  --white:#ffffff;
  --pale:#e6f1fb;
}
*{box-sizing:border-box;margin:0;padding:0}
html,body{width:1200px;height:3274px;overflow:hidden}
body{position:relative;background:var(--white);font-family:"Questrial",sans-serif;color:var(--ink)}

.hero{position:absolute;left:0;top:0;width:1200px;height:590px;overflow:hidden;
  background:linear-gradient(180deg,#4a5578 0%,#6c6f8e 35%,#8a7f92 55%,#3b3f55 80%,#2a2d3d 100%)}
.hero-photo{position:absolute;inset:0}
.hero-band{position:absolute;left:0;bottom:0;width:1200px;height:80px}
.brand-box{position:absolute;left:413px;top:-4px;width:355px;height:154px;border:2px solid #6fb6e3;border-top:none;border-radius:0 0 16px 16px;background:rgba(70,80,105,.75);display:flex;flex-direction:column;align-items:center;justify-content:center}
.brand-name{font-size:31px;letter-spacing:3px;color:#a9d3f0;text-transform:uppercase;margin-top:10px}
.brand-domain{font-size:9px;letter-spacing:2px;color:#a9d3f0;align-self:flex-end;margin-right:48px;margin-top:2px}
.hero-title{position:absolute;left:0;top:198px;width:1200px;text-align:center;font-size:42px;line-height:51px;color:var(--white);text-transform:uppercase;letter-spacing:-0.5px}
.hero-sub{position:absolute;left:0;top:384px;width:1200px;text-align:center;font-size:26px;line-height:34px;color:var(--white)}

.intro{position:absolute;left:0;top:590px;width:1200px;height:728px;overflow:hidden}
.intro-photo{position:absolute;left:0;top:190px;width:1200px;height:538px;
  background:linear-gradient(90deg,#b7bcc6 0%,#8e939e 30%,#cfd4dc 55%,#6b7280 75%,#d9dde3 100%)}
.intro-fade{position:absolute;left:0;top:190px;width:1200px;height:360px;background:linear-gradient(180deg,#fff 0%,rgba(255,255,255,.6) 50%,rgba(255,255,255,0) 100%)}
.intro-text{position:absolute;left:0;top:92px;width:1200px;text-align:center;font-size:31px;line-height:41px}
.intro-text strong{font-family:"Montserrat",sans-serif;font-weight:700;color:var(--accent-text);font-size:29px}
.btn{display:flex;align-items:center;justify-content:center;gap:14px;font-family:"Montserrat",sans-serif;font-weight:700;color:var(--white);font-size:16px;letter-spacing:.3px;border-radius:6px;background:linear-gradient(90deg,#5aa6dc 0%,#2d6fa8 60%,#1b4f85 100%);border:1px solid #1b4f85}
.btn-upload{position:absolute;left:449px;top:225px;width:300px;height:51px}

.enquiry{position:absolute;left:0;top:1318px;width:1200px;height:636px;background:linear-gradient(110deg,#ffffff 35%,var(--pale) 100%)}
.enquiry-title{position:absolute;left:0;top:76px;width:1218px;text-align:center;font-size:31px;line-height:41px}
.field{position:absolute;background:var(--white);border:1px solid var(--line);font-size:17px;color:var(--muted);padding:12px 12px}
.field-name{left:297px;top:207px;width:306px;height:45px}
.field-email{left:633px;top:207px;width:305px;height:45px;padding-left:27px}
.field-story{left:297px;top:268px;width:641px;height:180px;padding:16px 20px}
.btn-submit{position:absolute;left:530px;top:486px;width:140px;height:51px}

.gallery{position:absolute;left:149px;top:2007px;width:950px;display:grid;grid-template-columns:460px 460px;column-gap:30px;row-gap:19px}
.tile{height:258px;box-shadow:0 12px 24px rgba(0,0,0,.18)}
.t1{background:linear-gradient(180deg,#3a5f93 0%,#c78a4a 55%,#2e7fc2 100%)}
.t2{background:linear-gradient(180deg,#c77e73 0%,#3c3b33 50%,#6b5240 100%)}
.t3{background:linear-gradient(135deg,#1b6f98 0%,#2fa9b8 55%,#e8e4d6 80%,#3d6b3a 100%)}
.t4{background:linear-gradient(180deg,#5aa8e0 0%,#3c7a4a 25%,#47c4cf 55%,#7fd9d5 100%)}
.t5{background:linear-gradient(180deg,#1e6bb8 0%,#2f8fd8 50%,#1a3d6a 100%)}
.t6{background:linear-gradient(180deg,#8a5b57 0%,#c9b3a8 45%,#5a2f35 100%)}
.t7{background:linear-gradient(180deg,#2d7fb0 0%,#1b4a6e 50%,#e9e8ea 100%)}
.t8{background:linear-gradient(180deg,#7fb3e6 0%,#dfe9f3 35%,#3fb4c9 70%,#8a6c4a 100%)}

.footer{position:absolute;left:0;top:3169px;width:1200px;height:105px;background:var(--navy);color:#cfe0f0;font-size:11px;text-align:center;padding-top:46px;letter-spacing:.2px}
</style>
</head>
<body>

<header class="hero">
  <div class="hero-photo" role="img" aria-label="Resort terrace with palm trees and lanterns overlooking the sea at dusk"></div>
  <svg class="hero-band" viewBox="0 0 1200 80" width="1200" height="80">
    <polygon points="0,62 1200,0 1200,80 0,80" fill="#3aa8dc"/>
    <polygon points="0,72 1200,28 1200,80 0,80" fill="#1f5e95"/>
  </svg>
  <div class="brand-box">
    <div class="brand-name">Velvet Harbor</div>
    <div class="brand-domain">.COM.AU</div>
  </div>
  <h1 class="hero-title">Looking to stay at a 5 star<br>hotel or to fly business<br>class anywhere?</h1>
  <p class="hero-sub">Share a screenshot of your travel plans and<br>we beat the price, within 24 hours</p>
</header>

<section class="intro">
  <div class="intro-photo" role="img" aria-label="Chauffeur greeting travellers beside a limousine and crew by a private jet"></div>
  <div class="intro-fade"></div>
  <p class="intro-text">We work directly with hotels and airlines to<br>get you <strong>the best price,always</strong>.</p>
  <div class="btn btn-upload">
    <svg width="22" height="20" viewBox="0 0 22 20" fill="none" stroke="#fff" stroke-width="1.6">
      <rect x="1" y="4" width="16" height="14" rx="2"/>
      <polyline points="3,16 8,10 12,14 15,11 17,13"/>
      <line x1="18" y1="1" x2="18" y2="7"/><line x1="15" y1="4" x2="21" y2="4"/>
    </svg>
    ADD SCREENSHOOT HERE
  </div>
</section>

<section class="enquiry">
  <h2 class="enquiry-title" style="font-weight:400">Tell us about your next holiday plans.<br>The more details the better</h2>
  <div class="field field-name">Your full name</div>
  <div class="field field-email">Your email</div>
  <div class="field field-story">Tell your travel story here</div>
  <div class="btn btn-submit">SUBMIT</div>
</section>

<section class="gallery">
  <div class="tile t1" role="img" aria-label="Beachfront resort with illuminated pool at twilight"></div>
  <div class="tile t2" role="img" aria-label="Couple dining on a lantern-lit hillside terrace at sunset"></div>
  <div class="tile t3" role="img" aria-label="Aerial view of overwater villas in a turquoise lagoon"></div>
  <div class="tile t4" role="img" aria-label="Overwater villa with private pool and waterslide"></div>
  <div class="tile t5" role="img" aria-label="Underwater restaurant inside a glass aquarium tunnel"></div>
  <div class="tile t6" role="img" aria-label="Business class cabin suite with reclined seat"></div>
  <div class="tile t7" role="img" aria-label="Underwater bedroom suite looking into the ocean"></div>
  <div class="tile t8" role="img" aria-label="Infinity pool with daybed overlooking a tropical sea"></div>
</section>

<footer class="footer">©2022 VELVET HARBOR.COM.AU</footer>

</body>
</html>
```